Lumora business card for a plastic surgeon

we need a business card for plastic surgeons that work on a clinic called LUMORA.
we want a clean design and the following informations: name of the doctor, doctor's registration number (called CRM), telephone, address, facebook, instagram.
Colors: white, blue tones, light brown/ coffee

facebook and instagram: lumoracirurgiaestetica

Industry/Entity Type

Business

Contact Information for Business Card

clean design

Font styles to use
Serif
Sans Serif
Other font styles liked:
• helvetica light

Colors
cee9f5
85cae6
85abd2
3276b5
cfeae6
cedeed
eaf1f7

Requirements
Must have
• doctor's name
• identification number (called CRM)
• contact (phone, facebook, instagram, address)

```html
<!DOCTYPE html>
<html lang="pt">
<head>
<meta charset="utf-8">
<title>Lumora Cirurgia Plástica – Business Card</title>
<link rel="stylesheet" href="https://fonts.googleapis.com/css2?family=Cinzel:wght@400&family=Merriweather:wght@700&family=Roboto:wght@400&display=swap">
<style>
  :root{
    --backdrop:#e4e4e6;
    --paper:#f7f8fa;
    --paper-front:#eef3f9;
    --navy:#223f6b;
    --sky:#6cc0dc;
    --coffee:#ab998a;
    --ink:#1f3d6b;
    --white:#ffffff;
  }
  *{margin:0;padding:0;box-sizing:border-box}
  html,body{width:1200px;height:1200px;overflow:hidden;background:var(--backdrop)}
  .canvas{position:relative;width:1200px;height:1200px}

  .card{position:absolute;width:712px;height:418px;overflow:hidden;box-shadow:0 6px 14px rgba(0,0,0,.18)}
  .card-front{left:238px;top:119px;background:var(--paper-front)}
  .card-back{left:231px;top:644px;background:var(--paper)}

  .brand-name{font-family:"Cinzel",serif;font-weight:400;color:var(--sky);letter-spacing:2px;line-height:1;white-space:nowrap}
  .brand-tagline{font-family:"Cinzel",serif;font-weight:400;color:var(--ink);letter-spacing:1px;line-height:1;white-space:nowrap}

  .card-front .brand{position:absolute;left:0;right:0;top:148px;text-align:center}
  .card-front .brand-name{font-size:88px}
  .card-front .brand-tagline{font-size:32px;margin-top:16px}

  .back-shapes{position:absolute;inset:0}

  .doctor{position:absolute;right:37px;top:38px;text-align:right;color:var(--white)}
  .doctor-name{font-family:"Merriweather",serif;font-weight:700;font-size:26px;line-height:1}
  .doctor-crm{font-family:"Roboto",sans-serif;font-size:17px;margin-top:10px}

  .card-back .brand{position:absolute;left:30px;top:124px;text-align:center}
  .card-back .brand-name{font-size:72px}
  .card-back .brand-tagline{font-size:27px;margin-top:12px}

  .contact-list{position:absolute;right:37px;top:254px;list-style:none;font-family:"Roboto",sans-serif;font-size:18px;color:var(--ink);text-align:right}
  .contact-list li{display:flex;justify-content:flex-end;align-items:center;height:24.5px}
  .contact-list svg{width:18px;height:18px;margin-left:19px;fill:var(--coffee)}
  .address{position:absolute;right:37px;top:337px;font-family:"Roboto",sans-serif;font-size:18px;line-height:23px;color:var(--ink);text-align:right}

  .social-list{position:absolute;left:32px;top:334px;list-style:none;font-family:"Roboto",sans-serif;font-size:18px;color:var(--ink)}
  .social-list li{display:flex;align-items:center;height:24.5px}
  .social-mark{width:18px;height:18px;border-radius:4px;background:var(--coffee);margin-right:10px}
</style>
</head>
<body>
<main class="canvas">

  <section class="card card-front" aria-label="Card front">
    <div class="brand">
      <div class="brand-name">LUMORA</div>
      <div class="brand-tagline">CIRURGIA PLÁSTICA</div>
    </div>
  </section>

  <section class="card card-back" aria-label="Card back">
    <svg class="back-shapes" viewBox="0 0 712 418" width="712" height="418" aria-hidden="true">
      <path fill="var(--navy)" d="M0 0H712V185C600 178 520 135 420 84C330 38 220 12 130 18C70 23 30 34 0 45Z"/>
      <path fill="var(--coffee)" d="M0 50C80 27 200 16 300 30C340 37 370 52 392 64C330 46 250 38 170 43C100 48 40 62 0 82Z"/>
      <path fill="var(--sky)" d="M62 78C200 46 330 52 440 98C560 150 630 198 712 200V214C620 214 550 176 430 117C330 68 200 58 62 78Z"/>
    </svg>

    <div class="doctor">
      <div class="doctor-name">Dr. Lucas Moreira</div>
      <div class="doctor-crm">CRM: 123456789</div>
    </div>

    <div class="brand">
      <div class="brand-name">LUMORA</div>
      <div class="brand-tagline">CIRURGIA PLÁSTICA</div>
    </div>

    <ul class="contact-list">
      <li>+00 111 222 3333
        <svg viewBox="0 0 20 20"><path d="M2 8c0-3 3-5 8-5s8 2 8 5v1h-4V7H6v2H2zM5 10h10l2 7H3z"/></svg>
      </li>
      <li>www.yourwebsite.com
        <svg viewBox="0 0 20 20"><path d="M10 2a8 8 0 1 0 0 16a8 8 0 0 0 0-16zm0 1.5c1 1.3 1.7 3.3 1.9 5.7H8.1C8.3 6.8 9 4.8 10 3.5zM3.6 9.2h3c.1-2 .6-3.8 1.4-5a6.5 6.5 0 0 0-4.4 5zm0 1.6a6.5 6.5 0 0 0 4.4 5c-.8-1.2-1.3-3-1.4-5zm4.5 0h3.8c-.2 2.4-.9 4.4-1.9 5.7-1-1.3-1.7-3.3-1.9-5.7zm5.3 0c-.1 2-.6 3.8-1.4 5a6.5 6.5 0 0 0 4.4-5zm3-1.6a6.5 6.5 0 0 0-4.4-5c.8 1.2 1.3 3 1.4 5z"/></svg>
      </li>
      <li>yourname@yourwebsite.com
        <svg viewBox="0 0 20 20"><path d="M2 4h16v12H2zm2 2v.5l6 4.5 6-4.5V6zm0 3v5h12V9l-6 4.5z"/></svg>
      </li>
    </ul>

    <p class="address">Your Long Commercial or<br>business address in 2 line</p>

    <ul class="social-list">
      <li><span class="social-mark"></span>lumoracirurgiaestetica</li>
      <li><span class="social-mark"></span>lumoracirurgiaestetica</li>
    </ul>
  </section>

</main>
</body>
</html>
```